Swim School Certificates

We are looking to have some certificates designed for our Learn to Swim School. These will be handed out to our students when they complete each level. We will need different certificates for each level, however, we would like a consistent theme throughout, so each level may only have a slight variation. We are happy for you to just show us a couple of variations to begin with, so we can see how these would work. Then once we decide on the winning design, you can complete the rest.
The levels are:
Bubs 1
Bubs 2
Toddler 1
Toddler 2
Beginner 1
Beginner 2
Beginner 3
Stroke Development 1
Stroke Development 2
Advanced 1
Advanced 2
Squad
The Certificates should include:
Congratulations to:
(blank line for name)
You have completed (level name), Keep up the good work!!!
Signed: (blank line) Date: (blank line)
I've included a copy of our logo, and a copy of our governing bodies logo both of which should be included on the certificate.
I've also included some examples of certificates we like, to give you an idea of our style. We are happy for the bubs and toddler certificates to be more child focused, so they can included a kid friendly element to them, however this will need to reduce to a more simplistic design as the levels increase into beginner and stroke etc.
You can also look on our Facebook page to get an idea of what we do.
https://www.facebook.com/coralreefswimschool/?ref=bookmarks
We will also need editable source files upon completion as we may be looking to change the name of some classes in the future.
Please let us know if you need any of the files in other formats
Kind Regards
Maree

```html
<!DOCTYPE html>
<html lang="en">
<head>
<meta charset="utf-8">
<title>Coral Reef Swim School – Level Certificates</title>
<link rel="stylesheet" href="https://fonts.googleapis.com/css2?family=Alfa+Slab+One&family=Arvo:wght@700&display=swap">
<style>
  :root {
    --page: #ffffff;
    --paper: #ffffff;
    --sky: #a3e6f4;
    --sky-deep: #8fdcef;
    --stripe-light: #b4eaf6;
    --stripe-dark: #98dff0;
    --wave-deep: #5fb4ea;
    --wave-light: #9fd3f4;
    --ribbon: #5ac6e0;
    --ribbon-dark: #3d93a6;
    --ribbon-fold: #2f7a8b;
    --text-blue: #4cbde6;
    --brand-blue: #4aa9df;
    --name-red: #e02a1f;
    --rule: #555555;
    --dots: #7fcbe6;
    --badge: #2a7fc0;
    --illus-yellow: #e7e04a;
    --illus-red: #e2382a;
    --illus-kid: #2f8fd0;
  }
  html, body {
    margin: 0;
    padding: 0;
    width: 1200px;
    height: 1200px;
    overflow: hidden;
    background: var(--page);
  }
  .sheet { display: block; width: 1200px; height: 1200px; }
  .paper { fill: var(--paper); filter: url(#paper-shadow); }
  .heading { font-family: "Arvo", Georgia, serif; font-weight: 700; fill: var(--text-blue); text-anchor: middle; }
  .recipient { font-family: "Alfa Slab One", Georgia, serif; fill: var(--name-red); text-anchor: middle; }
  .level { font-family: "Alfa Slab One", Georgia, serif; fill: var(--name-red); text-anchor: middle; }
  .label { font-family: "Arvo", Georgia, serif; font-weight: 700; fill: var(--text-blue); }
  .rule { stroke: var(--rule); stroke-width: 1.6; }
  .dotted { fill: none; stroke: var(--dots); stroke-width: 2; stroke-dasharray: 1 4; stroke-linecap: round; }
  .brand { font-family: "Arvo", Georgia, serif; font-weight: 700; fill: var(--brand-blue); text-anchor: middle; }
  .badge { fill: var(--badge); }
  .ribbon-text { font-family: "Arvo", Georgia, serif; font-weight: 700; fill: #ffffff; font-size: 24px; letter-spacing: 1px; }
</style>
</head>
<body>
<svg class="sheet" viewBox="0 0 1200 1200" xmlns="http://www.w3.org/2000/svg">
  <defs>
    <filter id="paper-shadow" x="-10%" y="-10%" width="120%" height="125%">
      <feDropShadow dx="0" dy="8" stdDeviation="9" flood-color="#000" flood-opacity="0.18"/>
    </filter>
    <pattern id="stripes" width="40" height="72" patternUnits="userSpaceOnUse">
      <rect width="40" height="36" fill="var(--stripe-light)"/>
      <rect y="36" width="40" height="36" fill="var(--stripe-dark)"/>
    </pattern>
    <linearGradient id="wave-tone" x1="0" y1="0" x2="1" y2="1">
      <stop offset="0" stop-color="var(--wave-deep)"/>
      <stop offset="0.5" stop-color="var(--wave-light)"/>
      <stop offset="1" stop-color="var(--wave-deep)"/>
    </linearGradient>
    <path id="ribbon-curve" d="M170 706 Q305 654 440 706"/>
  </defs>

  <!-- Certificate: Bubs 1 -->
  <g class="certificate certificate--bubs">
    <rect class="paper" x="320" y="93" width="578" height="448"/>
    <rect x="346" y="114" width="524" height="405" rx="22" fill="var(--sky)"/>
    <g class="bubbles" fill="#c8f1fa">
      <circle cx="377" cy="230" r="17"/>
      <circle cx="369" cy="309" r="9"/>
      <circle cx="385" cy="350" r="10"/>
      <circle cx="843" cy="290" r="7"/>
      <circle cx="840" cy="409" r="16"/>
      <circle cx="786" cy="432" r="9"/>
    </g>
    <path class="cloud" fill="#ffffff"
      d="M440 215 A80 80 0 0 1 560 215 A80 80 0 0 1 680 215 A80 80 0 0 1 800 215
         A80 80 0 0 1 805 330 A80 80 0 0 1 800 440
         A80 80 0 0 1 680 440 A80 80 0 0 1 560 440 A80 80 0 0 1 440 440
         A80 80 0 0 1 430 330 A80 80 0 0 1 440 215 Z"/>
    <path class="dotted" transform="translate(620 328) scale(0.94) translate(-620 -328)"
      d="M440 215 A80 80 0 0 1 560 215 A80 80 0 0 1 680 215 A80 80 0 0 1 800 215
         A80 80 0 0 1 805 330 A80 80 0 0 1 800 440
         A80 80 0 0 1 680 440 A80 80 0 0 1 560 440 A80 80 0 0 1 440 440
         A80 80 0 0 1 430 330 A80 80 0 0 1 440 215 Z"/>

    <rect x="382" y="132" width="106" height="70" fill="#ffffff" opacity="0"/>
    <text class="brand" x="435" y="160" font-size="19">Coral Reef</text>
    <text class="brand" x="435" y="184" font-size="12">Swim School</text>

    <rect x="710" y="140" width="136" height="140" rx="60" fill="var(--illus-yellow)"
      role="img" aria-label="Illustration of a yellow swim cap with blue goggles"/>
    <rect x="346" y="384" width="134" height="120" rx="20" fill="var(--illus-red)"
      role="img" aria-label="Illustration of a pair of red swim fins"/>

    <text class="heading" x="612" y="248" font-size="16">Congratulations to:</text>
    <text class="recipient" x="612" y="294" font-size="31">Jane Doe</text>
    <line class="rule" x1="480" y1="306" x2="746" y2="306"/>
    <text class="heading" x="612" y="327" font-size="11">You have completed</text>
    <text class="level" x="612" y="352" font-size="17">Bubs 1</text>
    <line class="rule" x1="478" y1="358" x2="746" y2="358"/>
    <text class="heading" x="612" y="390" font-size="12.5">Keep up the good work!!!</text>
    <text class="label" x="480" y="423" font-size="9.5">Signed:</text>
    <line class="rule" x1="522" y1="423" x2="617" y2="423"/>
    <text class="label" x="620" y="423" font-size="9.5">Date:</text>
    <line class="rule" x1="653" y1="423" x2="746" y2="423"/>

    <circle class="badge" cx="818" cy="476" r="29" role="img" aria-label="Governing body registration badge"/>
  </g>

  <!-- Certificate: Toddler 1 -->
  <g class="certificate certificate--toddler">
    <rect class="paper" x="10" y="576" width="578" height="446"/>
    <rect x="38" y="597" width="523" height="405" rx="20" fill="url(#stripes)"/>
    <rect x="78" y="624" width="451" height="350" rx="16" fill="#ffffff"/>
    <rect class="dotted" x="96" y="638" width="416" height="322" rx="12"/>

    <g class="ribbon">
      <polygon points="120,697 165,686 172,734 128,740 142,718" fill="var(--ribbon-dark)"/>
      <polygon points="486,697 445,686 438,734 480,740 466,718" fill="var(--ribbon-dark)"/>
      <path d="M150 676 Q305 624 460 676 L460 720 Q305 668 150 720 Z" fill="var(--ribbon)"/>
      <text class="ribbon-text" text-anchor="middle">
        <textPath href="#ribbon-curve" startOffset="50%">CONGRATULATIONS</textPath>
      </text>
    </g>

    <text class="recipient" x="302" y="757" font-size="31">Jane Doe</text>
    <line class="rule" x1="170" y1="764" x2="437" y2="764"/>
    <text class="heading" x="302" y="781" font-size="11">You have completed</text>
    <text class="level" x="302" y="809" font-size="17">Toddler 1</text>
    <line class="rule" x1="168" y1="817" x2="437" y2="817"/>
    <text class="heading" x="302" y="845" font-size="12.5">Keep up the good work!!!</text>
    <text class="label" x="170" y="881" font-size="9.5">Signed:</text>
    <line class="rule" x1="212" y1="881" x2="307" y2="881"/>
    <text class="label" x="310" y="881" font-size="9.5">Date:</text>
    <line class="rule" x1="343" y1="881" x2="437" y2="881"/>

    <rect x="256" y="892" width="100" height="128" rx="40" fill="var(--illus-kid)"
      role="img" aria-label="Illustration of a smiling child in a blue swim cap and goggles"/>
    <circle class="badge" cx="471" cy="924" r="29" role="img" aria-label="Governing body registration badge"/>
  </g>

  <!-- Certificate: Beginner 1 -->
  <g class="certificate certificate--beginner">
    <rect class="paper" x="608" y="574" width="580" height="450"/>
    <rect x="634" y="596" width="527" height="406" rx="18" fill="url(#wave-tone)"
      role="img" aria-label="Blue and white wave pattern background"/>
    <ellipse cx="895" cy="792" rx="236" ry="188" fill="#ffffff"/>
    <ellipse class="dotted" cx="895" cy="792" rx="222" ry="176"/>

    <text class="brand" x="893" y="660" font-size="19">Coral Reef</text>
    <text class="brand" x="893" y="684" font-size="12">Swim School</text>

    <text class="heading" x="895" y="723" font-size="16">Congratulations to:</text>
    <text class="recipient" x="895" y="764" font-size="31">Jane Doe</text>
    <line class="rule" x1="762" y1="771" x2="1030" y2="771"/>
    <text class="heading" x="895" y="786" font-size="11">You have completed</text>
    <text class="level" x="895" y="816" font-size="17">Beginner 1</text>
    <line class="rule" x1="760" y1="824" x2="1030" y2="824"/>
    <text class="heading" x="895" y="851" font-size="12.5">Keep up the good work!!!</text>
    <text class="label" x="763" y="890" font-size="9.5">Signed:</text>
    <line class="rule" x1="805" y1="890" x2="900" y2="890"/>
    <text class="label" x="903" y="890" font-size="9.5">Date:</text>
    <line class="rule" x1="936" y1="890" x2="1030" y2="890"/>

    <circle class="badge" cx="894" cy="932" r="29" role="img" aria-label="Governing body registration badge"/>
  </g>
</svg>
</body>
</html>
```